Upscale business cards needed for Board of Directors

We need professional business cards created for members of our family business Board of Directors. We would like these relatively simple and straightforward, but also with a unique element to set them apart. Probably stick with neutral and simple colors - white, grey etc. We need space for the traditional elements, including name, title, address, email/phone number. And we will be creating several from this template so it needs to be template that is easy to switch information in and out of.
Business
See description

```html
<!DOCTYPE html>
<html lang="en">
<head>
<meta charset="utf-8">
<title>Harborline Holdings — Business Cards</title>
<link rel="stylesheet" href="https://fonts.googleapis.com/css2?family=Lato:ital,wght@0,400;0,900;1,400&display=swap">
<style>
  :root {
    --stage: #3a3a3a;
    --card: #050505;
    --gold: #b9a77f;
    --white: #ffffff;
  }
  * { margin: 0; padding: 0; box-sizing: border-box; }
  html, body { width: 1200px; height: 900px; overflow: hidden; }
  body {
    background: var(--stage);
    font-family: "Lato", sans-serif;
    color: var(--white);
  }
  .canvas {
    width: 1200px; height: 900px;
    display: flex; flex-direction: column;
    align-items: center; justify-content: center;
    gap: 60px;
  }
  .card {
    position: relative;
    width: 640px; height: 366px;
    background: var(--card);
    overflow: hidden;
  }
  .wordmark {
    font-weight: 900;
    color: var(--white);
    text-transform: uppercase;
    line-height: 1.05;
    letter-spacing: 0.04em;
  }
  /* Back */
  .card--back {
    display: flex; flex-direction: column;
    align-items: center; justify-content: center;
  }
  .card--back .wordmark { font-size: 40px; text-align: center; }
  .card--back .website {
    margin-top: 42px;
    font-size: 15px;
    letter-spacing: 0.12em;
  }
  /* Front */
  .card--front .wordmark {
    position: absolute; left: 40px; top: 40px;
    font-size: 34px;
  }
  .holder { position: absolute; left: 40px; top: 150px; }
  .holder__name {
    color: var(--gold);
    font-size: 19px;
    letter-spacing: 0.03em;
  }
  .holder__title { font-size: 14px; font-style: italic; margin-top: 2px; }
  .contact {
    position: absolute; left: 360px; top: 200px;
    font-size: 17px; line-height: 1.3;
  }
  .contact__address { margin-bottom: 6px; }
  .contact__row { display: flex; align-items: center; gap: 12px; }
  .contact__icon { width: 16px; height: 16px; flex: none; }
  .card__band {
    position: absolute; left: 0; right: 0; bottom: 0;
    height: 9px; background: var(--gold);
  }
</style>
</head>
<body>
<main class="canvas">
  <section class="card card--back" aria-label="Card back">
    <div class="wordmark">Harborline<br>Holdings</div>
    <div class="website">www.harborline.com</div>
  </section>

  <section class="card card--front" aria-label="Card front">
    <div class="wordmark">Harborline<br>Holdings</div>
    <div class="holder">
      <div class="holder__name">DANIEL MERCER</div>
      <div class="holder__title">Director</div>
    </div>
    <div class="contact">
      <div class="contact__address">1450 Oak Crest Dr<br>Cedar Falls TX 78010</div>
      <div class="contact__row">
        <svg class="contact__icon" viewBox="0 0 16 16" aria-hidden="true"><path fill="#b9a77f" d="M3.5 1.5l2.5 0 1 3.5-1.6 1.2a8 8 0 0 0 4.4 4.4L11 9l3.5 1v2.5c0 1-1 2-2 2C6.5 14.5 1.5 9.5 1.5 3.5c0-1 1-2 2-2z"/></svg>
        <span>512 555 0140</span>
      </div>
      <div class="contact__row">
        <svg class="contact__icon" viewBox="0 0 16 16" aria-hidden="true"><path fill="#b9a77f" d="M4 1h8v4H4zM2 6h12a1 1 0 0 1 1 1v5h-3v3H4v-3H1V7a1 1 0 0 1 1-1zm3 5v3h6v-3z"/></svg>
        <span>512 555 0141</span>
      </div>
      <div class="contact__row">
        <svg class="contact__icon" viewBox="0 0 16 16" aria-hidden="true"><path fill="#b9a77f" d="M1 3h14v10H1zm1.5 1.2L8 8.5l5.5-4.3z"/></svg>
        <span>info@harborline.com</span>
      </div>
      <div class="contact__row">
        <svg class="contact__icon" viewBox="0 0 16 16" aria-hidden="true"><g fill="none" stroke="#b9a77f" stroke-width="1.4"><circle cx="8" cy="8" r="6.5"/><ellipse cx="8" cy="8" rx="2.8" ry="6.5"/><path d="M1.5 8h13M2.5 4.8h11M2.5 11.2h11"/></g></svg>
        <span>www.harborline.com</span>
      </div>
    </div>
    <div class="card__band"></div>
  </section>
</main>
</body>
</html>
```